Redesign existing website

We would like a redesign of the website http://www.velbrisanalytics.com that creates a more modern, up to date look.

Velbris Analytics creates software for social science research and is focused on making the software user friendly and easy to use. We would like to convey seriousness, but also
a very up to date, just released look.

Feel free to modify the logo if you wish.

Target Market(s)

Academics, researchers

Industry/Entity Type

Software

Requirements
Must have
• The design should incorporate the same information as the current website.

```html
<!DOCTYPE html>
<html lang="en">
<head>
<meta charset="utf-8">
<title>Velbris Analytics</title>
<link rel="stylesheet" href="https://fonts.googleapis.com/css2?family=Cinzel:wght@700&family=Noto+Sans&family=Oswald:wght@500&family=Kaushan+Script&family=Arimo:wght@400;700&family=Open+Sans:wght@300&display=swap">
<style>
:root{
  --top-band:#756c63;
  --header:#4a413f;
  --nav-btn:#efefed;
  --nav-active:#1f1f1f;
  --panel:#ededeb;
  --mission-bg:#e5e3d1;
  --section:#d9d7d2;
  --rule:#a8a293;
  --ink:#2a2a2a;
  --orange:#e8791f;
  --orange-btn:#f36f0e;
  --news-title:#a05f16;
  --footer:#2f2c29;
  --footer-text:#b9b5ae;
  --white:#ffffff;
}
*{margin:0;padding:0;box-sizing:border-box}
html,body{width:1200px;height:1037px;overflow:hidden;background:var(--white)}
.canvas{position:relative;width:1200px;height:1037px;font-family:"Noto Sans",sans-serif;color:var(--ink)}
.abs{position:absolute}
.top-band{left:0;top:0;width:1200px;height:18px;background:var(--top-band)}
.site-header{left:0;top:46px;width:1200px;height:143px;background:var(--header)}
.brand-dot{left:255px;top:59px;width:64px;height:64px;border-radius:50%;background:#2a3f93;border:3px solid #e8e8e8}
.brand-name{left:100px;top:134px;width:375px;text-align:center;font-family:"Cinzel",serif;font-weight:700;font-size:24px;color:var(--white);letter-spacing:.5px}
.nav a{position:absolute;display:flex;align-items:center;justify-content:center;border-radius:6px;background:linear-gradient(#fafaf9,#e4e4e2);font-family:"Arimo",sans-serif;font-weight:700;font-size:17px;color:#222;text-decoration:none}
.nav a.active{background:linear-gradient(#4a4a4a,#141414);color:var(--white);font-weight:400;font-size:16px}
.hero{left:71px;top:209px;width:1101px;height:317px;background:var(--panel);border-radius:9px}
.hero-photo{left:114px;top:226px;width:655px;height:281px;background:linear-gradient(180deg,#d8d6d4 0%,#f0dccd 30%,#5f7a3c 52%,#6a6a52 68%,#4b5a4c 100%)}
.mission{left:797px;top:237px;width:332px;height:267px;background:var(--mission-bg);border-radius:8px}
.mission p{position:absolute;left:19px;width:300px;font-size:14px;line-height:17px;letter-spacing:.6px;color:#333}
.slider-ctrl{left:851px;top:461px;width:200px;height:43px;background:#ebebe9}
.section{left:0;top:560px;width:1200px;height:358px;background:var(--section)}
.rule{top:581px;width:1px;height:333px;background:var(--rule)}
.welcome-title{left:80px;top:590px;font-family:"Kaushan Script",cursive;font-size:30px;color:var(--orange)}
.welcome-photo{left:80px;top:642px;width:287px;height:122px;background:linear-gradient(180deg,#cfd7e0 0%,#f0d9c3 25%,#5e7a3a 50%,#6d7060 70%,#4a5b48 100%)}
.welcome-text{left:77px;top:774px;width:300px;font-size:14px;line-height:17px;letter-spacing:.6px;color:#333}
.read-more{left:71px;top:870px;width:92px;height:21px;border-radius:11px;background:var(--orange-btn);color:var(--white);font-family:"Arimo",sans-serif;font-weight:700;font-size:14px;text-align:center;line-height:21px}
.news-head{left:461px;top:591px;width:273px;height:45px;border:1px solid var(--rule);font-size:20px;color:var(--news-title);padding:9px 0 0 18px;letter-spacing:.5px}
.news-item{left:469px;width:270px;font-size:14px;line-height:17px;letter-spacing:.5px;color:#222}
.login{left:840px;top:591px;width:310px;height:277px;border-radius:6px;background:linear-gradient(#fbfbfb,#e6e6e5)}
.login-title{left:20px;top:29px;font-family:"Oswald",sans-serif;font-weight:500;font-size:20px;color:#222;letter-spacing:-.3px}
.login label{position:absolute;left:20px;font-family:"Arimo",sans-serif;font-size:13px;color:#222}
.login .field{position:absolute;left:20px;width:255px;height:35px;background:var(--white);border:1px solid #ddd;border-radius:9px}
.login-btn{left:20px;top:207px;font-family:"Oswald",sans-serif;font-weight:500;font-size:19px;color:#f4f4f4;text-shadow:0 0 1px #aaa}
.signup{left:128px;top:214px;font-family:"Arimo",sans-serif;font-size:13px;color:#222;text-decoration:underline}
.site-footer{left:0;top:928px;width:1200px;height:109px;background:var(--footer)}
.footer-nav{left:0;top:970px;width:1200px;text-align:center;font-family:"Open Sans",sans-serif;font-weight:300;font-size:15px;color:var(--footer-text);word-spacing:4px}
.copyright{left:0;top:993px;width:1200px;text-align:center;font-family:"Cinzel",serif;font-weight:700;font-size:12px;color:var(--footer-text)}
</style>
</head>
<body>
<div class="canvas">
  <div class="abs top-band"></div>

  <header class="abs site-header"></header>
  <div class="abs brand-dot"></div>
  <div class="abs brand-name">VELBRIS ANALYTICS</div>
  <nav class="nav">
    <a class="active" style="left:557px;top:137px;width:106px;height:42px">Home</a>
    <a style="left:676px;top:141px;width:103px;height:38px">Products</a>
    <a style="left:788px;top:141px;width:103px;height:38px">news</a>
    <a style="left:900px;top:141px;width:102px;height:38px">about us</a>
    <a style="left:1013px;top:141px;width:104px;height:38px">contact us</a>
  </nav>

  <section class="abs hero"></section>
  <div class="abs hero-photo" role="img" aria-label="Photo of a lakeside town with red-roofed houses under a pale sky"></div>
  <div class="abs mission">
    <p style="top:38px">The mission of Velbris Analytics, Inc. is to produce software products that multiply the power and efficiency of empirical scientific research in the social sciences.</p>
    <p style="top:122px">A central goal is to expand access to complex data sources and to the advanced methods of scientific investigation needed to analyze them.</p>
  </div>
  <div class="abs slider-ctrl"></div>
  <svg class="abs" style="left:851px;top:461px" width="200" height="43" viewBox="0 0 200 43">
    <defs><linearGradient id="btn" x1="0" y1="0" x2="0" y2="1"><stop offset="0" stop-color="#fdfdfd"/><stop offset="1" stop-color="#dcdcdc"/></linearGradient></defs>
    <circle cx="26" cy="27" r="21" fill="url(#btn)" stroke="#cfcfcf"/>
    <path d="M29 20 L22 27 L29 34" fill="none" stroke="#222" stroke-width="3"/>
    <circle cx="171" cy="27" r="21" fill="url(#btn)" stroke="#cfcfcf"/>
    <path d="M168 20 L175 27 L168 34" fill="none" stroke="#222" stroke-width="3"/>
    <circle cx="75" cy="29" r="4" fill="#333"/>
    <circle cx="91" cy="29" r="4" fill="#c8c8c8"/>
    <circle cx="108" cy="29" r="4" fill="#c8c8c8"/>
    <circle cx="124" cy="29" r="4" fill="#c8c8c8"/>
  </svg>

  <section class="abs section"></section>
  <div class="abs rule" style="left:420px"></div>
  <div class="abs rule" style="left:789px"></div>

  <h2 class="abs welcome-title">Welcome</h2>
  <div class="abs welcome-photo" role="img" aria-label="Photo of a lakeside town with trees along the shore"></div>
  <p class="abs welcome-text">The mission of Velbris Analytics, Inc. is to produce software products that multiply the power and efficiency of empirical scientific research in the social sciences.</p>
  <div class="abs read-more">Read More</div>

  <h3 class="abs news-head" style="font-weight:400">Latest News</h3>
  <p class="abs news-item" style="top:657px">September 07, 2011</p>
  <p class="abs news-item" style="top:692px">Lorem ipsum dolor sit amet, consectetuer adipi scing elit. Praesent vestibum molestie lacus. Aenean nonummy</p>
  <p class="abs news-item" style="top:775px">September 05, 2011</p>
  <p class="abs news-item" style="top:810px">Lorem ipsum dolor sit amet, consectetuer adipi scing elit. Praesent vestibum molestie lacus. Aenean nonummy</p>

  <div class="abs login">
    <div class="abs login-title">USER LOGIN</div>
    <label style="top:78px">Enter username:</label>
    <div class="field" style="top:95px"></div>
    <label style="top:140px">Enter password:</label>
    <div class="field" style="top:157px"></div>
    <div class="abs login-btn">LOGIN</div>
    <div class="abs signup">Don't have account yet?</div>
  </div>

  <footer class="abs site-footer"></footer>
  <div class="abs footer-nav">home &nbsp;/ &nbsp;products &nbsp;/ &nbsp;news &nbsp;/ &nbsp;about us &nbsp;/ &nbsp;contact us</div>
  <div class="abs copyright"><span style="font-family:'Open Sans',sans-serif;font-weight:300;font-size:20px;vertical-align:-2px">©</span> VELBRIS ANALYTICS.com</div>
</div>
</body>
</html>
```